Company letterhead, compliments slip and business card design for Electrical Contracting Company
Colm Dwyer Electrical
Corporate
Declan Dwyer
Managing DIrector
Cloon
Mullan Road
Dunmara
Arden
declan@colmdwyer.com
www.colmdwyer.com

```html
<!DOCTYPE html>
<html lang="en">
<head>
<meta charset="utf-8">
<title>Colm Dwyer Electrical – Stationery</title>
<link href="https://fonts.googleapis.com/css2?family=Montserrat:wght@400;600;700&family=Great+Vibes&display=swap" rel="stylesheet">
<style>
:root{
  --red:#c8102e;
  --red-dark:#9e0c23;
  --ink:#2a2a2a;
  --charcoal:#333333;
  --charcoal-deep:#1c1c1c;
  --grey:#8c8c8c;
  --rule:#d6d6d6;
  --paper:#ffffff;
  --backdrop:#dcdcdc;
}
*{box-sizing:border-box;margin:0;padding:0}
html,body{width:1200px;height:1025px;overflow:hidden;background:var(--backdrop)}
body{font-family:"Montserrat",Arial,sans-serif;color:var(--ink)}
.canvas{position:relative;width:1200px;height:1025px;overflow:hidden}
.set{position:absolute;left:0;width:1200px;height:510px}
.set--one{top:0}
.set--two{top:512px}
.piece{position:absolute;background:var(--paper);box-shadow:0 1px 3px rgba(0,0,0,.18)}

.mark{display:flex;align-items:center;gap:.4em;font-weight:700;color:var(--ink);white-space:nowrap;line-height:1}
.mark i{display:block;width:1.3em;height:1.3em;background:var(--red);flex:none}
.mark--light{color:var(--paper)}
.mark--light.on-red i{background:var(--paper)}

.small{font-size:5px;line-height:1.5;color:var(--grey)}
.tagline{font-size:6px;letter-spacing:.18em;text-transform:uppercase;color:var(--grey);margin-top:6px}

/* folder */
.folder-cover{left:33px;top:55px;width:204px;height:315px;
  background:radial-gradient(ellipse at 50% 45%,#4a4a4a 0%,var(--charcoal) 45%,var(--charcoal-deep) 100%);
  display:flex;flex-direction:column;justify-content:center;padding-left:22px}
.folder-cover .mark{font-size:9px}
.folder-inside{left:237px;top:55px;width:209px;height:315px;padding:18px 16px}
.folder-inside .mark{font-size:7px}
.folder-inside::after{content:"";position:absolute;left:0;right:0;bottom:10px;height:2px;background:var(--red)}
.folder-pocket{left:33px;top:370px;width:413px;height:130px;background:transparent;box-shadow:none}
.folder-pocket svg{display:block}
.pocket-contact{position:absolute;left:22px;bottom:20px}
.pocket-mark{position:absolute;right:22px;bottom:22px;font-size:6px}
.set--two .folder-cover .mark{font-size:8px}

/* business cards */
.card{top:83px;width:90px;height:55px;padding:8px}
.card .mark{font-size:5px}
.card--front::after{content:"";position:absolute;left:0;right:0;bottom:0;height:4px;background:var(--red)}
.card--details .name{font-size:5px;font-weight:700}
.card--details .role{font-size:3.5px;color:var(--red);margin-bottom:4px}
.card--details .small{font-size:3.5px}
.card--dark{background:linear-gradient(135deg,#474747,var(--charcoal-deep));display:flex;align-items:center;justify-content:center}
.card--red{background:var(--red);display:flex;align-items:center;justify-content:center}

/* letterhead */
.letterhead{top:144px;width:202px;height:285px;padding:14px 14px}
.letterhead .mark{font-size:6px}
.letterhead .head{display:flex;justify-content:space-between;align-items:flex-start}
.letterhead .head .small{font-size:3.5px;text-align:right}
.letterhead::after{content:"";position:absolute;left:0;right:0;bottom:0;height:6px;background:var(--red)}
.letterhead .foot{position:absolute;left:14px;right:14px;bottom:9px;font-size:3px;color:var(--grey);text-align:center}
.sheet-table{margin-top:22px;width:100%;border-collapse:collapse;font-size:3.5px;color:var(--ink)}
.sheet-table td{border:.5px solid var(--rule);padding:2px 3px;height:8px}
.sheet-table th{background:var(--charcoal);color:var(--paper);font-weight:600;text-align:left;padding:2px 3px}
.ticks{display:flex;gap:12px;margin-top:8px;font-size:3.5px;color:var(--grey)}
.ticks span::before{content:"";display:inline-block;width:4px;height:4px;border:.5px solid var(--grey);margin-right:2px;vertical-align:-1px}

/* compliments slips */
.slip{left:907px;width:223px;height:100px;padding:10px 12px}
.slip .mark{font-size:6px}
.slip .greeting{font-family:"Great Vibes",cursive;font-size:17px;color:var(--ink);margin-top:24px}
.slip .small{position:absolute;right:12px;top:10px;font-size:3.5px;text-align:right}
.slip::after{content:"";position:absolute;left:0;right:0;bottom:0;height:4px;background:var(--red)}
.slip .topline{position:absolute;left:0;right:0;top:0;height:4px;background:var(--charcoal)}

/* envelopes */
.envelope{left:907px;width:230px;height:105px;overflow:hidden}
.envelope svg{position:absolute;left:0;top:0}
.envelope .mark{position:absolute;left:12px;top:10px;font-size:5px}
.envelope .small{position:absolute;left:12px;top:22px;font-size:3px}
.envelope--white{top:280px}
.envelope--dark{top:336px;background:var(--charcoal)}
.envelope--red{top:392px;background:var(--red)}
.envelope--dark .mark,.envelope--red .mark{left:50%;top:14px;transform:translateX(-50%)}
</style>
</head>
<body>
<main class="canvas">

  <section class="set set--one" aria-label="Stationery set, first layout">
    <div class="piece folder-cover">
      <div class="mark mark--light"><i></i><span>Colm Dwyer Electrical</span></div>
      <div class="tagline">Electrical Contractors</div>
    </div>
    <div class="piece folder-inside">
      <div class="mark"><i></i><span>Colm Dwyer Electrical</span></div>
    </div>
    <div class="piece folder-pocket">
      <svg width="413" height="130" viewBox="0 0 413 130">
        <path d="M0 0 H190 L204 40 L218 0 H413 V130 H0 Z" fill="#ffffff"/>
        <line x1="204" y1="40" x2="204" y2="130" stroke="#e2e2e2" stroke-width="1"/>
        <rect x="204" y="124" width="209" height="2" fill="#c8102e"/>
      </svg>
      <div class="pocket-contact small">Cloon, Mullan Road, Dunmara, Arden<br>www.colmdwyer.com</div>
      <div class="mark pocket-mark"><i></i><span>Colm Dwyer Electrical</span></div>
    </div>

    <div class="piece card card--front" style="left:502px"><div class="mark"><i></i><span>Colm Dwyer Electrical</span></div></div>
    <div class="piece card card--details" style="left:600px">
      <div class="name">Declan Dwyer</div>
      <div class="role">Managing Director</div>
      <div class="small">Cloon, Mullan Road, Dunmara<br>T 000 000 0000<br>declan@colmdwyer.com</div>
    </div>
    <div class="piece card card--dark" style="left:698px"><div class="mark mark--light"><i></i><span>Colm Dwyer Electrical</span></div></div>
    <div class="piece card card--red" style="left:800px"><div class="mark mark--light on-red"><i></i><span>Colm Dwyer Electrical</span></div></div>

    <div class="piece letterhead" style="left:460px">
      <div class="head">
        <div class="mark"><i></i><span>Colm Dwyer Electrical</span></div>
        <div class="small">Cloon, Mullan Road<br>Dunmara, Arden<br>T 000 000 0000</div>
      </div>
      <table class="sheet-table">
        <tr><th>Date</th><td></td><th>Invoice No.</th><td></td></tr>
        <tr><th>Customer</th><td></td><th>Job Ref.</th><td></td></tr>
        <tr><th>Description</th><td></td><th>Amount</th><td></td></tr>
        <tr><td></td><td></td><td></td><td></td></tr>
        <tr><td></td><td></td><th>Total</th><td></td></tr>
      </table>
      <div class="ticks"><span>Paid</span><span>Due</span><span>Quote</span></div>
      <div class="foot">declan@colmdwyer.com · www.colmdwyer.com</div>
    </div>
    <div class="piece letterhead" style="left:683px">
      <div class="head">
        <div class="mark"><i></i><span>Colm Dwyer Electrical</span></div>
        <div class="small">Cloon, Mullan Road<br>Dunmara, Arden<br>T 000 000 0000</div>
      </div>
      <div class="foot">declan@colmdwyer.com · www.colmdwyer.com</div>
    </div>

    <div class="piece slip" style="top:28px">
      <div class="mark"><i></i><span>Colm Dwyer Electrical</span></div>
      <div class="small">Cloon, Mullan Road<br>Dunmara, Arden</div>
      <div class="greeting">With Compliments</div>
    </div>
    <div class="piece slip" style="top:153px">
      <div class="topline"></div>
      <div class="mark" style="margin-top:4px"><i></i><span>Colm Dwyer Electrical</span></div>
      <div class="small" style="top:14px">www.colmdwyer.com</div>
    </div>

    <div class="piece envelope envelope--white">
      <div class="mark"><i></i><span>Colm Dwyer Electrical</span></div>
      <div class="small">If undelivered return to sender</div>
    </div>
    <div class="piece envelope envelope--dark">
      <svg width="230" height="105" viewBox="0 0 230 105"><path d="M0 0 L115 45 L230 0 Z" fill="#4a4a4a"/></svg>
      <div class="mark mark--light"><i></i><span>Colm Dwyer Electrical</span></div>
    </div>
    <div class="piece envelope envelope--red">
      <svg width="230" height="105" viewBox="0 0 230 105"><path d="M0 0 L115 45 L230 0 Z" fill="#9e0c23"/></svg>
      <div class="mark mark--light on-red"><i></i><span>Colm Dwyer Electrical</span></div>
    </div>
  </section>

  <section class="set set--two" aria-label="Stationery set, second layout">
    <div class="piece folder-cover">
      <div class="mark mark--light"><i></i><span>Colm Dwyer Electrical</span></div>
    </div>
    <div class="piece folder-inside">
      <div class="mark"><i></i><span>Colm Dwyer Electrical</span></div>
    </div>
    <div class="piece folder-pocket">
      <svg width="413" height="130" viewBox="0 0 413 130">
        <path d="M0 0 H190 L204 40 L218 0 H413 V130 H0 Z" fill="#ffffff"/>
        <line x1="204" y1="40" x2="204" y2="130" stroke="#e2e2e2" stroke-width="1"/>
        <rect x="204" y="124" width="209" height="2" fill="#c8102e"/>
      </svg>
      <div class="pocket-contact small">Cloon, Mullan Road, Dunmara, Arden<br>www.colmdwyer.com</div>
      <div class="mark pocket-mark"><i></i><span>Colm Dwyer Electrical</span></div>
    </div>

    <div class="piece card card--front" style="left:502px"><div class="mark"><i></i><span>Colm Dwyer Electrical</span></div></div>
    <div class="piece card card--details" style="left:600px">
      <div class="name">Declan Dwyer</div>
      <div class="role">Managing Director</div>
      <div class="small">Cloon, Mullan Road, Dunmara<br>T 000 000 0000<br>declan@colmdwyer.com</div>
    </div>
    <div class="piece card card--dark" style="left:698px"><div class="mark mark--light"><i></i><span>Colm Dwyer Electrical</span></div></div>
    <div class="piece card card--red" style="left:800px"><div class="mark mark--light on-red"><i></i><span>Colm Dwyer Electrical</span></div></div>

    <div class="piece letterhead" style="left:460px">
      <div class="head">
        <div class="mark"><i></i><span>Colm Dwyer Electrical</span></div>
        <div class="small">Cloon, Mullan Road<br>Dunmara, Arden<br>T 000 000 0000</div>
      </div>
      <table class="sheet-table">
        <tr><th>Date</th><td></td><th>Invoice No.</th><td></td></tr>
        <tr><th>Customer</th><td></td><th>Job Ref.</th><td></td></tr>
        <tr><th>Description</th><td></td><th>Amount</th><td></td></tr>
        <tr><td></td><td></td><td></td><td></td></tr>
        <tr><td></td><td></td><th>Total</th><td></td></tr>
      </table>
      <div class="ticks"><span>Paid</span><span>Due</span><span>Quote</span></div>
      <div class="foot">declan@colmdwyer.com · www.colmdwyer.com</div>
    </div>
    <div class="piece letterhead" style="left:683px">
      <div class="head">
        <div class="mark"><i></i><span>Colm Dwyer Electrical</span></div>
        <div class="small">Cloon, Mullan Road<br>Dunmara, Arden<br>T 000 000 0000</div>
      </div>
      <div class="foot">declan@colmdwyer.com · www.colmdwyer.com</div>
    </div>

    <div class="piece slip" style="top:28px">
      <div class="mark"><i></i><span>Colm Dwyer Electrical</span></div>
      <div class="small">Cloon, Mullan Road<br>Dunmara, Arden</div>
      <div class="greeting">With Compliments</div>
    </div>
    <div class="piece slip" style="top:153px">
      <div class="topline"></div>
      <div class="mark" style="margin-top:4px"><i></i><span>Colm Dwyer Electrical</span></div>
      <div class="small" style="top:14px">www.colmdwyer.com</div>
    </div>

    <div class="piece envelope envelope--white">
      <div class="mark"><i></i><span>Colm Dwyer Electrical</span></div>
      <div class="small">If undelivered return to sender</div>
    </div>
    <div class="piece envelope envelope--dark">
      <svg width="230" height="105" viewBox="0 0 230 105"><path d="M0 0 L115 45 L230 0 Z" fill="#4a4a4a"/></svg>
      <div class="mark mark--light"><i></i><span>Colm Dwyer Electrical</span></div>
    </div>
    <div class="piece envelope envelope--red">
      <svg width="230" height="105" viewBox="0 0 230 105"><path d="M0 0 L115 45 L230 0 Z" fill="#9e0c23"/></svg>
      <div class="mark mark--light on-red"><i></i><span>Colm Dwyer Electrical</span></div>
    </div>
  </section>

</main>
</body>
</html>
```